High Tech Software Startup needs Letterhead Design

We need a letterhead for a startup company base in Brazil. The letterhead should combine with our logo attached here.
We are a team of professionals in Java for web and mobile with iOS and android development.
We are looking for a modern and futuristc design.

Target Market(s)

CIO, IT managers of mid to big size companies

Industry/Entity Type

It Company

```html
<!DOCTYPE html>
<html lang="pt-BR">
<head>
<meta charset="utf-8">
<title>TAVRIQ Letterhead</title>
<link href="https://fonts.googleapis.com/css2?family=Source+Sans+3:wght@400;600;700;800&display=swap" rel="stylesheet">
<style>
  :root {
    --paper: #ffffff;
    --paper-shade: #e4e8ec;
    --navy: #1f2f55;
    --bar-start: #08a8e6;
    --bar-mid: #1a7fb0;
    --bar-end: #2d3f6c;
    --contact-text: #7b8188;
  }
  html, body {
    margin: 0;
    padding: 0;
    width: 850px;
    height: 1200px;
    overflow: hidden;
    background: var(--paper);
  }
  .letterhead {
    position: relative;
    width: 850px;
    height: 1200px;
    overflow: hidden;
    background: var(--paper);
    font-family: "Source Sans 3", "Myriad Pro", Arial, sans-serif;
  }
  .paper-texture {
    position: absolute;
    inset: 0;
    background:
      radial-gradient(ellipse 420px 620px at 58% 48%, var(--paper) 30%, rgba(255,255,255,0) 100%),
      linear-gradient(135deg, var(--paper-shade) 0%, var(--paper) 45%, var(--paper) 60%, var(--paper-shade) 100%);
  }
  .brand {
    position: absolute;
    left: 62px;
    top: 55px;
    height: 55px;
    display: flex;
    align-items: center;
    gap: 10px;
  }
  .brand-square {
    width: 55px;
    height: 55px;
    border-radius: 4px;
    background: var(--bar-mid);
  }
  .brand-name {
    font-weight: 800;
    font-size: 56px;
    line-height: 1;
    letter-spacing: 1px;
    color: var(--navy);
  }
  .header-bar {
    position: absolute;
    left: 369px;
    top: 64px;
    width: 481px;
    height: 39px;
    background: linear-gradient(90deg, var(--bar-start) 0%, var(--bar-mid) 45%, var(--bar-end) 100%);
  }
  .contact-block {
    position: absolute;
    left: 644px;
    top: 1071px;
    font-size: 11.5px;
    line-height: 14.5px;
    color: var(--contact-text);
    letter-spacing: -0.1px;
  }
  .contact-block p {
    margin: 0;
  }
  .contact-address {
    margin-bottom: 14.5px !important;
  }
</style>
</head>
<body>
  <div class="letterhead">
    <div class="paper-texture" role="img" aria-label="Soft diagonal line texture fading toward the centre of the page"></div>

    <div class="brand">
      <div class="brand-square"></div>
      <div class="brand-name">TAVRIQ</div>
    </div>
    <div class="header-bar"></div>

    <div class="contact-block">
      <p class="contact-address">
        Rua das Acácias, 418&nbsp; 9º.<br>
        Andar&nbsp; Conj. 902 Caixa Postal&nbsp; 317<br>
        Bela Vista&nbsp;&nbsp;&nbsp; CEP&nbsp; 01.234-560<br>
        São Paulo - SP - Brasil
      </p>
      <p>
        Phone: (11) 5555-0142<br>
        Website: www.tavriq.com.br<br>
        E-mail: contato@tavriq.com.br
      </p>
    </div>
  </div>
</body>
</html>
```